Baufirma sucht Design für Schafkopfkarten
Zielgruppe
Wir sind eine Baufirma und suchen ein schlichtes Design für unsere Schafkopfkarten. Unsere Zielgruppe ist bunt gemischt
Aufgabenstellung
Wir suchen nach einem Design für Schafkopfkarten/Spielkarten.
- Kartenformat 56 x 100 mm
- weißer Rand
- Schlicht
- eventuell Retro Design
- Firmenlogo soll nicht verändert werden
- eventuell 'seit 1946' integrieren

```html
<!DOCTYPE html>
<html lang="de">
<head>
<meta charset="utf-8">
<title>Warnholm Spielkarte</title>
<link rel="stylesheet" href="https://fonts.googleapis.com/css2?family=Unbounded:wght@700;800&family=Archivo:wght@400&display=swap">
<style>
  :root {
    --page-bg: #8a8a8a;
    --card-white: #ffffff;
    --panel-light: #ececee;
    --panel-dark: #e2e2e5;
    --brand-yellow: #ffd91a;
    --brand-dark: #45484d;
    --brand-grey: #7b7d81;
    --tagline-grey: #6a6b6e;
  }
  * { margin: 0; padding: 0; box-sizing: border-box; }
  html, body {
    width: 688px;
    height: 1200px;
    overflow: hidden;
    background: var(--page-bg);
  }
  .card {
    position: absolute;
    left: 36px;
    top: 50px;
    width: 616px;
    height: 1100px;
    background: var(--card-white);
    box-shadow: 0 4px 14px rgba(0,0,0,0.25);
  }
  .card-frame {
    position: absolute;
    inset: 0;
  }
  .half {
    position: absolute;
    left: 0;
    top: 0;
    width: 616px;
    height: 550px;
  }
  .half--flipped {
    top: 550px;
    transform: rotate(180deg);
  }
  .since-label {
    position: absolute;
    left: 63px;
    top: 52px;
    font-family: "Unbounded", sans-serif;
    font-weight: 800;
    font-size: 27px;
    letter-spacing: 0.5px;
    color: var(--brand-dark);
  }
  .brand-mark {
    position: absolute;
    left: 286px;
    top: 235px;
    width: 44px;
    height: 44px;
    background: var(--brand-yellow);
  }
  .brand-name {
    position: absolute;
    left: 0;
    width: 616px;
    top: 318px;
    text-align: center;
    font-family: "Unbounded", sans-serif;
    font-weight: 800;
    font-size: 50px;
    line-height: 1;
    color: var(--brand-dark);
  }
  .services {
    position: absolute;
    left: 0;
    width: 616px;
    top: 396px;
    text-align: center;
    font-family: "Archivo", sans-serif;
    font-weight: 400;
    font-size: 21px;
    letter-spacing: 0.8px;
    color: var(--tagline-grey);
    white-space: nowrap;
  }
  .services .separator {
    color: var(--brand-yellow);
    margin: 0 10px;
  }
  .divider {
    position: absolute;
    left: 74px;
    top: 544px;
    width: 470px;
    height: 11px;
    display: flex;
  }
  .divider span { flex: 1; }
  .divider .seg-dark { background: var(--brand-dark); }
  .divider .seg-grey { background: var(--brand-grey); }
  .divider .seg-yellow { background: var(--brand-yellow); }
</style>
</head>
<body>
  <div class="card">
    <svg class="card-frame" width="616" height="1100" viewBox="0 0 616 1100" aria-hidden="true">
      <defs>
        <linearGradient id="panelShade" x1="0" y1="0" x2="0" y2="1">
          <stop offset="0" stop-color="var(--panel-dark)"/>
          <stop offset="0.5" stop-color="var(--panel-light)"/>
          <stop offset="1" stop-color="var(--panel-dark)"/>
        </linearGradient>
      </defs>
      <path class="frame-line" fill="none" stroke="var(--brand-yellow)" stroke-width="4.5"
        d="M44,138 Q44,113 69,113 L265,113 Q290,113 290,88 L290,70 Q290,39 321,39 L547,39 Q572,39 572,64 L572,962 Q572,987 547,987 L351,987 Q326,987 326,1012 L326,1030 Q326,1061 295,1061 L69,1061 Q44,1061 44,1036 Z"/>
      <path class="frame-panel" fill="url(#panelShade)"
        d="M56,145 Q56,125 76,125 L263,125 Q302,125 302,86 L302,71 Q302,51 322,51 L540,51 Q560,51 560,71 L560,955 Q560,975 540,975 L353,975 Q314,975 314,1014 L314,1029 Q314,1049 294,1049 L76,1049 Q56,1049 56,1029 Z"/>
    </svg>

    <div class="half">
      <div class="since-label">SEIT 1946</div>
      <div class="brand-mark"></div>
      <div class="brand-name">WARNHOLM</div>
      <div class="services">TIEFBAU<span class="separator">//</span>ABBRUCH<span class="separator">//</span>RECYCLING</div>
    </div>

    <div class="half half--flipped">
      <div class="since-label">SEIT 1946</div>
      <div class="brand-mark"></div>
      <div class="brand-name">WARNHOLM</div>
      <div class="services">TIEFBAU<span class="separator">//</span>ABBRUCH<span class="separator">//</span>RECYCLING</div>
    </div>

    <div class="divider">
      <span class="seg-dark"></span>
      <span class="seg-grey"></span>
      <span class="seg-yellow"></span>
    </div>
  </div>
</body>
</html>
```